Revolutionary Video Platform (uncoded) - updated 05.11.

We want you to design the frontpage (uncoded) of KELVORAMATCH.net (we ev. hire the winner to create the subpages).

The concept of KELVORAMATCH.net is to show (ONLY!) infield videos of dating coaches (when they get in contact with women on the street) so that the users will have a solid base for deciding which coach they want to contact. I highlight that because some designs contained other ideas like "dating tips". No, we are specialized on infield videos. People should see if these coaches are really worth their money.

Therefore, the frontpage must include the following:

Header: Logo (attached), writing "KELVORAMATCH" or "KELVORA MATCH", links "Contact", "About", "Sign In", "Sign Up"

No design yet tried to change the logo in its size. You're welcome to do creative stuff.

What else is necessary on the front page:

1. 2 statements:

"Because 34 videos prove how to get every woman you want."
"Connect directly with 26 dating-coaches from these videos!"

The numbers should be showed in a way that the users know that they count up automatically; important: use the style zimpel has on it's front page by showing their amount of users.

2. Top rated Dating Coaches:

As the videos on the site can be rated, we want the coaches with the best rated videos on the front page with their faces (people can jump from there directly to their profiles).

To the pictures of the coaches you should also add the country flag and the city (where they come from). Plus, users should see who's on the first place, who's on the second place.. max. 10 coaches on the front page..

Set the title "TOP 10 DATING COACHES listed by best rated videos"

3. Search System

In order to find the videos the user is searching for, it needs a simple search form, where they can search after:

- Language
- Country
- City
- Rating
- Level of Difficulty
- Set-Size
- Conversation Starter

You can use simple white bars with a drop-down button.

4. Tags

Implement tags like "bitch shield, blow out opener, bounce, calibration, canned routine, challenge point, cockblock, cold approach, cold reading, compliment opener" etc.

Alphabetically listed..

5. Create previews of the (searched) videos which contains:

- Thumbnail of the video (only thumbnails on front page, no bigger video playback window, pls use pictures in order to make the site look more real)

- Some infos about the video (name of the coach with user-picture, duration, language, country (name and flag), city, audio comment (yes/no), difficulty level (super easy-expert), views, points needed to view (1-3), 5 star rating)

- Title and the beginning of the text about the video (written by the coach), i.e. about 30 words

- There are 2 sorts of videos.. (it's not necessary to explain why, it's just important that you implement two different versions of the video preview area (different only in terms of color!).. for example, some video preview areas could be edged in gold, others in silver.. or you could fill the whole video preview area with a color.. show me your taste... even though I prefer the more elegant way like gold and silver, you can probably surprise me with other color combinations..

- In order to simplify the process of comparing your designs, pls create 4 such preview video are areas..

6. Best voted video reviewer:

Users AND coaches will be able to write reviews about the videos. These reviews can be liked/voted. Therefore, we will know which user or coach writes the best reviews.

So we want you to implement also the charts of the 10 best voted video reviewers. Make sure there is a ranking list with the name of the user/coach and how many likes he got.
Here as well: add country flag, country and city (to see where they come from)..plus a little thumbnail of the profile picture.. Make sure the best 3 are being highlighted somehow..
Updates

Some designs were quite creative so far.
But unfortunately, less than half of the designers considered all requirements.
Therefore, be sure to implement all the requirements (for example, check new point nr. 6).
Without considering all the requirements, you don't have a chance to win this content.

Thank you.

Target Market(s)

male, 16-40 years old, worldwide audience

Industry/Entity Type

Dating

Requirements
Must have
• Not all submitted designs considered all requirements.

Therefore, please read the requirements carefully and consider all of them. If you want to add some new ideas or if you decide not to implement some requirements, I suggest to submit a second design.
Nice to have
• - if you have other ideas, feel free to add some of them to the front page, probably in form of a second design

- sometimes the same page will look totally different in other colors. Therefore, it would be great to add a 2nd version of your design, in terms of color

- the front page needs to be an eye-catcher

- different KELVORAMATCH font styles (come up with your own taste), a few different styles would be great!
Should not have
• - a search field like there is one in the first submitted design (the intelligent search is already being available with the filter system and the tags)

- female colors like pink/purple (it's a site only for men)

- a 08/15 look.. this will be the first website worldwide which contains videos from the best dating gurus on this planet in action.. they deserve a cool place to show their videos in order to gain new customers..

```html
<!DOCTYPE html>
<html lang="en">
<head>
<meta charset="utf-8">
<title>KELVORAMATCH.net – Infield videos</title>
<link rel="stylesheet" href="https://fonts.googleapis.com/css2?family=Noto+Sans:wght@400;700&family=Open+Sans:wght@400;600&display=swap">
<style>
:root{
  --page-bg:#ffffff;
  --panel-bg:#f2f2f2;
  --panel-rule:#ffffff;
  --panel-edge:#d8d8d8;
  --link-blue:#2a4f8a;
  --text-dark:#111111;
  --text-muted:#8a8a8a;
  --gold-top:#e6c42a;
  --gold-bottom:#c99d12;
  --silver-top:#8a8a8a;
  --silver-bottom:#5a5a5a;
  --bronze-top:#b98646;
  --bronze-bottom:#93602a;
  --star-on:#f2c200;
  --star-off:#cfcfcf;
  --footer-top:#ececec;
  --footer-bottom:#d4d4d4;
  --footer-text:#555555;
  --thumb-sky:#2aa0f0;
  --thumb-sea:#1a6fd0;
}
*{margin:0;padding:0;box-sizing:border-box}
html,body{width:1200px;height:771px;overflow:hidden;background:var(--page-bg)}
body{position:relative;font-family:"Noto Sans",Verdana,sans-serif;color:var(--text-dark)}

/* video list */
.video-list{position:absolute;left:130px;top:0;width:620px;height:693px;background:var(--panel-bg);border-bottom:3px solid var(--panel-edge)}
.video-card{position:absolute;left:0;width:620px;height:234px}
.video-card + .video-card{border-top:2px solid var(--panel-rule)}
.coach-avatar{position:absolute;left:26px;top:0;width:41px;height:41px;background:#fff;border:1px solid #dcdcdc;border-radius:2px}
.coach-name{position:absolute;left:79px;top:11px;font-size:13px;color:var(--link-blue);letter-spacing:.3px}
.points{position:absolute;right:32px;top:11px;font-size:13px;color:var(--link-blue);letter-spacing:.4px}
.thumb{position:absolute;left:26px;top:52px;width:186px;height:154px;background:linear-gradient(180deg,var(--thumb-sky) 0%,#3d8ee0 45%,var(--thumb-sea) 60%,#0d47a8 100%);overflow:hidden}
.thumb .curl{position:absolute;right:0;bottom:0}
.video-title{position:absolute;left:226px;top:46px;font-size:13px;font-weight:700;color:var(--link-blue);text-decoration:underline;letter-spacing:.35px}
.video-text{position:absolute;left:227px;top:72px;width:360px;font-size:13px;line-height:16px}
.rating{position:absolute;left:226px;top:111px;display:flex;align-items:center;gap:5px}
.rating .score{font-size:11px;margin-left:8px;letter-spacing:.5px}
.audio{position:absolute;left:227px;top:140px;font-size:11px;letter-spacing:.4px}
.audio a{color:var(--link-blue);text-decoration:none}
.meta{position:absolute;top:165px;font-size:11px;line-height:14px;color:var(--text-muted);letter-spacing:.4px}
.meta.views{left:226px}.meta.lang{left:367px}.meta.place{left:503px}

.flag{display:inline-block;position:relative;width:15px;height:10px;vertical-align:-1px;margin-left:4px;background:repeating-linear-gradient(180deg,#d33 0 1.43px,#fff 1.43px 2.86px);border:1px solid #9aa}
.flag::before{content:"";position:absolute;left:0;top:0;width:7px;height:5px;background:#2d4fa0}

/* reviewers */
.sidebar-title{position:absolute;width:265px;left:800px;text-align:center;font-family:"Open Sans",Arial,sans-serif;font-size:16px}
.podium{position:absolute;left:800px;width:265px;height:43px;border-radius:2px;color:#fff}
.podium.gold{background:linear-gradient(180deg,var(--gold-top),var(--gold-bottom))}
.podium.silver{background:linear-gradient(180deg,var(--silver-top),var(--silver-bottom))}
.podium.bronze{background:linear-gradient(180deg,var(--bronze-top),var(--bronze-bottom))}
.podium .avatar{position:absolute;left:8px;top:7px;width:29px;height:29px;border:1px solid #fff}
.podium .name{position:absolute;left:48px;top:6px;font-size:11px;font-weight:700;letter-spacing:.6px}
.podium .from{position:absolute;left:48px;top:22px;font-size:11px;letter-spacing:.4px}
.podium .likes{position:absolute;right:9px;top:14px;font-size:11px;letter-spacing:.5px}
.podium .likes b{font-weight:700}
.reviewer{position:absolute;left:808px;width:257px;height:30px}
.reviewer .avatar{position:absolute;left:0;top:2px;width:24px;height:24px;border:1px solid #ccc}
.reviewer .name{position:absolute;left:31px;top:0;font-size:11px;font-weight:700;letter-spacing:.7px}
.reviewer .from{position:absolute;left:31px;top:15px;font-size:9px;color:var(--text-muted);letter-spacing:.5px}
.reviewer .likes{position:absolute;left:193px;top:1px;font-size:10px;color:var(--text-muted);letter-spacing:.6px}
.reviewer .likes b{font-weight:700}

/* tags */
.tag{position:absolute;font-family:"Open Sans",Arial,sans-serif;color:var(--text-dark);text-decoration:none;white-space:nowrap;line-height:1}

/* footer */
.site-footer{position:absolute;left:0;top:717px;width:1200px;height:54px;background:linear-gradient(180deg,var(--footer-top),var(--footer-bottom))}
.copyright{position:absolute;left:505px;top:22px;font-size:11px;color:var(--footer-text);letter-spacing:.6px}
.back-top{position:absolute;left:990px;top:22px;font-size:11px;color:var(--footer-text);letter-spacing:.6px;text-decoration:none}
</style>
</head>
<body>

<main class="video-list">
  <!-- card 1 -->
  <article class="video-card" style="top:-3px">
    <div class="coach-avatar"></div>
    <span class="coach-name">Donec consequat</span>
    <span class="points">need 50 points</span>
    <div class="thumb" role="img" aria-label="Video thumbnail: blue sea at dusk with harbour lights">
      <svg class="curl" width="30" height="14" viewBox="0 0 30 14"><path d="M0 14 Q8 2 30 0 L30 14 Z" fill="#e6e6e6"/></svg>
    </div>
    <a class="video-title">Nunc blandit, augue vel auctor. Nam euismod velit.</a>
    <p class="video-text">Elementum ligula, quis congue nunc nisl eu urna. Nam euismod velit aliquam massa.</p>
    <div class="rating">
      <svg width="114" height="18" viewBox="0 0 114 18"><g id="s"><polygon points="9,0 11.6,6 18,6.6 13.1,10.8 14.6,17.2 9,13.8 3.4,17.2 4.9,10.8 0,6.6 6.4,6" fill="var(--star-on)"/></g><use href="#s" x="24"/><use href="#s" x="48"/><use href="#s" x="72" style="fill:var(--star-off)"/><polygon transform="translate(72 0)" points="9,0 11.6,6 18,6.6 13.1,10.8 14.6,17.2 9,13.8 3.4,17.2 4.9,10.8 0,6.6 6.4,6" fill="var(--star-off)"/><polygon transform="translate(96 0)" points="9,0 11.6,6 18,6.6 13.1,10.8 14.6,17.2 9,13.8 3.4,17.2 4.9,10.8 0,6.6 6.4,6" fill="var(--star-off)"/></svg>
      <span class="score">(4.4/5)</span>
    </div>
    <p class="audio">Audio comment: <a>No</a></p>
    <p class="meta views">62 221 views<br>Difficulty: Medium</p>
    <p class="meta lang">Language: English<br>3:22</p>
    <p class="meta place">USA <span class="flag"></span><br>New York</p>
  </article>

  <!-- card 2 -->
  <article class="video-card" style="top:219px;padding-top:12px">
    <div class="coach-avatar" style="top:12px"></div>
    <span class="coach-name" style="top:23px">Donec consequat</span>
    <span class="points" style="top:23px">need 50 points</span>
    <div class="thumb" style="top:65px" role="img" aria-label="Video thumbnail: blue sea at dusk with harbour lights">
      <svg class="curl" width="30" height="14" viewBox="0 0 30 14"><path d="M0 14 Q8 2 30 0 L30 14 Z" fill="#e6e6e6"/></svg>
    </div>
    <a class="video-title" style="top:59px">Nunc blandit, augue vel auctor. Nam euismod velit.</a>
    <p class="video-text" style="top:85px">Elementum ligula, quis congue nunc nisl eu urna. Nam euismod velit aliquam massa.</p>
    <div class="rating" style="top:124px">
      <svg width="114" height="18" viewBox="0 0 114 18"><use href="#s"/><use href="#s" x="24"/><use href="#s" x="48"/><polygon transform="translate(72 0)" points="9,0 11.6,6 18,6.6 13.1,10.8 14.6,17.2 9,13.8 3.4,17.2 4.9,10.8 0,6.6 6.4,6" fill="var(--star-off)"/><polygon transform="translate(96 0)" points="9,0 11.6,6 18,6.6 13.1,10.8 14.6,17.2 9,13.8 3.4,17.2 4.9,10.8 0,6.6 6.4,6" fill="var(--star-off)"/></svg>
      <span class="score">(4.4/5)</span>
    </div>
    <p class="audio" style="top:153px">Audio comment: <a>No</a></p>
    <p class="meta views" style="top:178px">62 221 views<br>Difficulty: Medium</p>
    <p class="meta lang" style="top:178px">Language: English<br>3:22</p>
    <p class="meta place" style="top:178px">USA <span class="flag"></span><br>New York</p>
  </article>

  <!-- card 3 -->
  <article class="video-card" style="top:453px">
    <div class="coach-avatar" style="top:15px"></div>
    <span class="coach-name" style="top:26px">Donec consequat</span>
    <span class="points" style="top:26px">need 50 points</span>
    <div class="thumb" style="top:68px" role="img" aria-label="Video thumbnail: blue sea at dusk with harbour lights">
      <svg class="curl" width="30" height="14" viewBox="0 0 30 14"><path d="M0 14 Q8 2 30 0 L30 14 Z" fill="#e6e6e6"/></svg>
    </div>
    <a class="video-title" style="top:62px">Nunc blandit, augue vel auctor. Nam euismod velit.</a>
    <p class="video-text" style="top:88px">Elementum ligula, quis congue nunc nisl eu urna. Nam euismod velit aliquam massa.</p>
    <div class="rating" style="top:127px">
      <svg width="114" height="18" viewBox="0 0 114 18"><use href="#s"/><use href="#s" x="24"/><use href="#s" x="48"/><polygon transform="translate(72 0)" points="9,0 11.6,6 18,6.6 13.1,10.8 14.6,17.2 9,13.8 3.4,17.2 4.9,10.8 0,6.6 6.4,6" fill="var(--star-off)"/><polygon transform="translate(96 0)" points="9,0 11.6,6 18,6.6 13.1,10.8 14.6,17.2 9,13.8 3.4,17.2 4.9,10.8 0,6.6 6.4,6" fill="var(--star-off)"/></svg>
      <span class="score">(4.4/5)</span>
    </div>
    <p class="audio" style="top:156px">Audio comment: <a>No</a></p>
    <p class="meta views" style="top:181px">62 221 views<br>Difficulty: Medium</p>
    <p class="meta lang" style="top:181px">Language: English<br>3:22</p>
    <p class="meta place" style="top:181px">USA <span class="flag"></span><br>New York</p>
  </article>
</main>

<aside>
  <h2 class="sidebar-title" style="top:15px;font-weight:400">Best rated reviewers</h2>

  <div class="podium gold" style="top:69px"><div class="avatar" role="img" aria-label="Reviewer photo" style="background:#2a5a9a"></div><span class="name">Commodo Egestas</span><span class="from">New York in USA <span class="flag"></span></span><span class="likes"><b>1248</b> likes</span></div>
  <div class="podium silver" style="top:116px"><div class="avatar" role="img" aria-label="Reviewer photo" style="background:#1d4a86"></div><span class="name">Commodo Egestas</span><span class="from">New York in USA <span class="flag"></span></span><span class="likes"><b>1248</b> likes</span></div>
  <div class="podium bronze" style="top:163px"><div class="avatar" role="img" aria-label="Reviewer photo" style="background:#3a5f9a"></div><span class="name">Commodo Egestas</span><span class="from">New York in USA <span class="flag"></span></span><span class="likes"><b>1248</b> likes</span></div>

  <div class="reviewer" style="top:217px"><div class="avatar" role="img" aria-label="Reviewer photo" style="background:#c98a2a"></div><span class="name">Commodo EgestaS</span><span class="from">New York in USA <span class="flag"></span></span><span class="likes"><b>1248</b> likes</span></div>
  <div class="reviewer" style="top:253px"><div class="avatar" role="img" aria-label="Reviewer photo" style="background:#9a5a3a"></div><span class="name">Commodo EgestaS</span><span class="from">New York in USA <span class="flag"></span></span><span class="likes"><b>1248</b> likes</span></div>
  <div class="reviewer" style="top:291px"><div class="avatar" role="img" aria-label="Reviewer photo" style="background:#6a9aaa"></div><span class="name">Commodo EgestaS</span><span class="from">New York in USA <span class="flag"></span></span><span class="likes"><b>1248</b> likes</span></div>
  <div class="reviewer" style="top:327px"><div class="avatar" role="img" aria-label="Reviewer photo" style="background:#8a4a2a"></div><span class="name">Commodo EgestaS</span><span class="from">New York in USA <span class="flag"></span></span><span class="likes"><b>1248</b> likes</span></div>
  <div class="reviewer" style="top:363px"><div class="avatar" role="img" aria-label="Reviewer photo" style="background:#6aa08a"></div><span class="name">Commodo EgestaS</span><span class="from">New York in USA <span class="flag"></span></span><span class="likes"><b>1248</b> likes</span></div>
  <div class="reviewer" style="top:401px"><div class="avatar" role="img" aria-label="Reviewer photo" style="background:#2a5a7a"></div><span class="name">Commodo EgestaS</span><span class="from">New York in USA <span class="flag"></span></span><span class="likes"><b>1248</b> likes</span></div>
  <div class="reviewer" style="top:437px"><div class="avatar" role="img" aria-label="Reviewer photo" style="background:#c07a2a"></div><span class="name">Commodo EgestaS</span><span class="from">New York in USA <span class="flag"></span></span><span class="likes"><b>1248</b> likes</span></div>

  <h2 class="sidebar-title" style="top:496px;font-weight:400;font-size:15px">Tags</h2>
  <nav class="tags">
    <a class="tag" style="left:806px;top:532px;font-size:19px">cockblock</a>
    <a class="tag" style="left:906px;top:540px;font-size:10px">canned routine</a>
    <a class="tag" style="left:986px;top:528px;font-size:13px;text-align:center">compliment<br>opener</a>
    <a class="tag" style="left:845px;top:562px;font-size:25px">bounce</a>
    <a class="tag" style="left:945px;top:573px;font-size:12px">blow out opener</a>
    <a class="tag" style="left:808px;top:603px;font-size:13px">cold approach</a>
    <a class="tag" style="left:904px;top:603px;font-size:13px">calibration</a>
    <a class="tag" style="left:978px;top:599px;font-size:17px">bitch shield</a>
    <a class="tag" style="left:849px;top:629px;font-size:25px">challenge point</a>
  </nav>
</aside>

<footer class="site-footer">
  <p class="copyright">Copyright © 2012 All rights reserved.</p>
  <a class="back-top">Back to top
    <svg width="9" height="9" viewBox="0 0 9 9" style="margin-left:4px;vertical-align:0"><path d="M1 5 L4.5 1.5 L8 5 M1 8.5 L4.5 5 L8 8.5" fill="none" stroke="#555" stroke-width="1.2"/></svg>
  </a>
</footer>

</body>
</html>
```